Oven Cleaning Business owner needs business card design

Hi there,
Would like for a business card to be designed for myself, the owner of a professional oven cleaning business on the Sunshine Coast.
Would like it to look sleek, and modern-ish. Bit creative is encouraged too.
Include following:
Name/title: Corin ter Haghe, Owner
Phone number: 1300 482 916
Email: info@hearthshinecrew.com.au
Website: www.hearthshinecrew.com.au

```html
<!DOCTYPE html>
<html lang="en">
<head>
<meta charset="utf-8">
<title>Hearthshine Crew – Business Card</title>
<link rel="stylesheet" href="https://fonts.googleapis.com/css2?family=Montserrat:wght@400;500;600;800&display=swap">
<style>
  :root {
    --backdrop: #3a3a3c;
    --navy: #1b275a;
    --cyan: #1fd6d8;
    --ink: #1d1d1f;
    --paper: #ffffff;
    --paper-shade: #f2f2f4;
  }
  * { box-sizing: border-box; margin: 0; padding: 0; }
  html, body { width: 1200px; height: 1200px; overflow: hidden; }
  body {
    background: var(--backdrop);
    font-family: "Montserrat", Arial, sans-serif;
    position: relative;
  }
  .card {
    position: absolute;
    left: 220px;
    width: 760px;
    height: 434px;
    border-radius: 28px;
    overflow: hidden;
    box-shadow: 0 14px 30px rgba(0,0,0,0.35);
  }
  .card-front {
    top: 120px;
    background: linear-gradient(180deg, var(--paper) 0%, var(--paper-shade) 100%);
  }
  .card-back {
    top: 640px;
    background: var(--navy);
  }
  .front-wave { position: absolute; inset: 0; width: 760px; height: 434px; }
  .contact-block {
    position: absolute;
    left: 58px;
    top: 118px;
  }
  .person {
    border-left: 5px solid var(--cyan);
    padding-left: 12px;
    margin-bottom: 26px;
  }
  .person-name {
    color: var(--cyan);
    font-weight: 500;
    font-size: 27px;
    letter-spacing: -0.5px;
    text-transform: uppercase;
    line-height: 1;
  }
  .person-title {
    color: var(--ink);
    font-size: 17px;
    font-weight: 400;
    text-transform: uppercase;
    line-height: 1.2;
    margin-top: 2px;
  }
  .contact-list { list-style: none; margin-left: 18px; }
  .contact-item {
    display: flex;
    align-items: center;
    gap: 12px;
    color: var(--ink);
    font-size: 17px;
    line-height: 1;
    margin-bottom: 11px;
  }
  .contact-item:first-child { font-size: 20px; }
  .contact-icon { width: 20px; height: 20px; flex: none; }
  .brand {
    position: absolute;
    display: flex;
    flex-direction: column;
    align-items: center;
    text-align: center;
    color: var(--cyan);
    font-weight: 800;
    text-transform: uppercase;
    line-height: 1;
  }
  .brand-dot {
    border-radius: 50%;
    background: var(--cyan);
  }
  .brand-front { right: 70px; top: 62px; font-size: 38px; letter-spacing: 2px; }
  .brand-front .brand-dot { width: 70px; height: 70px; margin-bottom: 18px; }
  .brand-back { left: 0; right: 0; top: 118px; font-size: 58px; letter-spacing: 3px; }
  .brand-back .brand-dot { width: 96px; height: 96px; margin-bottom: 26px; }
</style>
</head>
<body>
  <section class="card card-front">
    <svg class="front-wave" viewBox="0 0 760 434" aria-hidden="true">
      <path d="M0 434 L0 392 C120 330 260 330 430 300 C600 270 700 210 760 140 L760 434 Z" fill="#1b275a"/>
      <path d="M420 312 C580 296 690 232 748 146 L760 140 L760 158 C700 246 590 302 420 314 Z" fill="#1fd6d8"/>
    </svg>

    <div class="brand brand-front">
      <span class="brand-dot"></span>
      <span class="brand-name">Hearthshine<br>Crew</span>
    </div>

    <div class="contact-block">
      <div class="person">
        <p class="person-name">Corin ter Haghe</p>
        <p class="person-title">Owner</p>
      </div>
      <ul class="contact-list">
        <li class="contact-item">
          <svg class="contact-icon" viewBox="0 0 24 24"><path fill="#1fd6d8" d="M6.6 10.8a15.2 15.2 0 0 0 6.6 6.6l2.2-2.2a1 1 0 0 1 1-.25 11.4 11.4 0 0 0 3.6.57 1 1 0 0 1 1 1V20a1 1 0 0 1-1 1A17 17 0 0 1 3 4a1 1 0 0 1 1-1h3.5a1 1 0 0 1 1 1c0 1.25.2 2.45.57 3.57a1 1 0 0 1-.25 1z"/></svg>
          <span>1300 482 916</span>
        </li>
        <li class="contact-item">
          <svg class="contact-icon" viewBox="0 0 24 24"><rect x="2" y="5" width="20" height="14" rx="1" fill="#1fd6d8"/><path d="M2 6 L12 13 L22 6" fill="none" stroke="#fff" stroke-width="1.6"/></svg>
          <span>info@hearthshinecrew.com.au</span>
        </li>
        <li class="contact-item">
          <svg class="contact-icon" viewBox="0 0 24 24" fill="none" stroke="#1fd6d8" stroke-width="1.8"><circle cx="12" cy="12" r="9.5"/><ellipse cx="12" cy="12" rx="4" ry="9.5"/><path d="M2.5 12h19M4 7h16M4 17h16"/></svg>
          <span>www.hearthshinecrew.com.au</span>
        </li>
      </ul>
    </div>
  </section>

  <section class="card card-back">
    <div class="brand brand-back">
      <span class="brand-dot"></span>
      <span class="brand-name">Hearthshine<br>Crew</span>
    </div>
  </section>
</body>
</html>
```